Stationery design bilingual preschool
Meadowlark preschool
Stationery design bilingual preschool - Childcare
Creative Brief
Bright & Fun-filled
Marita Sundqvist
Preschool director
Lövhagsvägen 9 128 31 Skarpnäck Sweden
angsfagelforskolan@postlada.se
www.angsfagelforskolan.com
Back of the business card suppose to have the same information as the front side but on Swedish.
(Subtitle) Ängsfågel Förskola AB ( name) Marita Sundqvist (title) Förskolechef (address) Lövhagsvägen 9 128 31 Skarpnäck (phone) Tel. 08 731 94 62 (cell) Mob. 073 862 40 15 (email) angsfagelforskolan@postlada.com (web side) www.angsfagelforskolan. com
butterfly2004 butterfly2004
Dear designers, I'd like to see design drafts ideas for the following products: 1. Business card 2. Letterhead 3. Envelope 4. Folder 5. CD and CD cover 6. Email signature 7. Presentation 8.Thank you card 8. Stamp 9. T-shirt, Hoody, Winter jacket/ Rain jacket, Cap, Scarf 10. Pen 11. Meadowlark character toy Thank you, PH

```html
<!DOCTYPE html>
<html lang="en">
<head>
<meta charset="utf-8">
<title>Meadowlark Preschool – Business Card</title>
<link href="https://fonts.googleapis.com/css2?family=Open+Sans:wght@400;600;700;800&display=swap" rel="stylesheet">
<style>
  :root {
    --bg: #e9ebe6;
    --green-dark: #2f8f1a;
    --green: #4cb52a;
    --green-light: #8fdc3f;
    --orange: #f39a1e;
    --white: #ffffff;
    --ink: #4a4a4a;
    --ink-soft: #7a7a7a;
    --rule: #cfcfcf;
  }
  * { margin: 0; padding: 0; box-sizing: border-box; }
  html, body { width: 1200px; height: 871px; overflow: hidden; }
  body {
    background: var(--bg);
    font-family: "Open Sans", Arial, sans-serif;
    display: flex; align-items: center; justify-content: center;
  }
  .card-set { display: flex; gap: 50px; }
  .card {
    position: relative; width: 540px; height: 310px;
    border-radius: 16px; overflow: hidden;
    box-shadow: 0 10px 28px rgba(0,0,0,.18);
  }

  /* Back side */
  .card--back {
    background: radial-gradient(ellipse at 50% 45%, var(--green-light) 0%, var(--green) 45%, var(--green-dark) 100%);
    display: flex; flex-direction: column; align-items: center; justify-content: center;
  }
  .card--back .brand { font-size: 40px; }
  .card--back .brand-dot { width: 26px; height: 26px; background: var(--white); }
  .card--back .brand-name { color: var(--white); }
  .back-url { margin-top: 14px; color: var(--white); font-size: 11px; font-weight: 600; letter-spacing: .3px; }

  /* Brand mark */
  .brand { display: flex; align-items: center; gap: 12px; font-weight: 800; line-height: 1.05; }
  .brand-dot { border-radius: 50%; flex: none; }
  .brand-name { letter-spacing: -.5px; }

  /* Front side */
  .card--front { background: var(--white); }
  .front-swoosh { position: absolute; inset: 0; }
  .holder { position: absolute; right: 26px; top: 28px; text-align: right; color: var(--white); }
  .holder-name { font-size: 17px; font-weight: 700; }
  .holder-title { font-size: 11px; font-weight: 600; margin-top: 3px; }

  .card--front .brand { position: absolute; left: 26px; top: 150px; font-size: 25px; gap: 10px; }
  .card--front .brand-dot { width: 20px; height: 20px; background: var(--orange); }
  .card--front .brand-name { color: var(--green); }

  .contact {
    position: absolute; left: 272px; top: 138px;
    border-left: 1px solid var(--rule); padding-left: 14px;
    list-style: none; font-size: 11.5px; color: var(--ink);
  }
  .contact li { display: flex; align-items: center; gap: 8px; height: 19px; }
  .contact li.addr { height: auto; align-items: flex-start; margin-top: 3px; line-height: 1.35; }
  .contact svg { width: 11px; height: 11px; flex: none; fill: var(--green); }
</style>
</head>
<body>
<main class="card-set">

  <section class="card card--back" aria-label="Business card back">
    <div class="brand">
      <span class="brand-dot"></span>
      <span class="brand-name">Meadowlark<br>Preschool</span>
    </div>
    <p class="back-url">www.angsfagelforskolan.com</p>
  </section>

  <section class="card card--front" aria-label="Business card front">
    <svg class="front-swoosh" viewBox="0 0 540 310" preserveAspectRatio="none" aria-hidden="true">
      <defs>
        <linearGradient id="swooshGreen" x1="0" y1="0" x2="1" y2="1">
          <stop offset="0" stop-color="#8fdc3f"/>
          <stop offset="1" stop-color="#2f8f1a"/>
        </linearGradient>
      </defs>
      <path d="M0 0 H540 V148 C420 92 230 60 0 64 Z" fill="url(#swooshGreen)"/>
      <path d="M150 68 C300 70 440 100 540 150 V170 C440 118 300 80 150 68 Z" fill="var(--orange)"/>
    </svg>

    <div class="holder">
      <p class="holder-name">Marita Sundqvist</p>
      <p class="holder-title">Preschool director</p>
    </div>

    <div class="brand">
      <span class="brand-dot"></span>
      <span class="brand-name">Meadowlark<br>Preschool</span>
    </div>

    <ul class="contact">
      <li><svg viewBox="0 0 24 24"><path d="M6.6 10.8a15 15 0 0 0 6.6 6.6l2.2-2.2c.3-.3.7-.4 1-.2 1.1.4 2.3.6 3.6.6.6 0 1 .4 1 1V20c0 .6-.4 1-1 1A17 17 0 0 1 3 4c0-.6.4-1 1-1h3.5c.6 0 1 .4 1 1 0 1.3.2 2.5.6 3.6.1.3 0 .7-.2 1z"/></svg>46 8 731 94 62</li>
      <li><svg viewBox="0 0 24 24"><path d="M7 1h10a2 2 0 0 1 2 2v18a2 2 0 0 1-2 2H7a2 2 0 0 1-2-2V3a2 2 0 0 1 2-2zm0 3v14h10V4z"/></svg>46 73 862 40 15</li>
      <li><svg viewBox="0 0 24 24"><path d="M2 5h20v14H2zm2 2v.5l8 5 8-5V7z"/></svg>angsfagelforskolan@postlada.se</li>
      <li><svg viewBox="0 0 24 24"><path d="M12 2a10 10 0 1 0 0 20 10 10 0 0 0 0-20zm0 2c1 1.3 1.8 3 2.2 5H9.8C10.2 7 11 5.3 12 4zM4.3 11h3.4c0 .7 0 1.4.1 2H4.3a8 8 0 0 1 0-2zm5.5 0h4.4a12 12 0 0 1 0 2H9.8a12 12 0 0 1 0-2zm6.5 0h3.4a8 8 0 0 1 0 2h-3.4c.1-.6.1-1.3 0-2zM9.8 15h4.4c-.4 2-1.2 3.7-2.2 5-1-1.3-1.8-3-2.2-5z"/></svg>www.angsfagelforskolan.com</li>
      <li class="addr"><svg viewBox="0 0 24 24"><path d="M12 2a7 7 0 0 0-7 7c0 5 7 13 7 13s7-8 7-13a7 7 0 0 0-7-7zm0 9.5A2.5 2.5 0 1 1 12 6.5a2.5 2.5 0 0 1 0 5z"/></svg><span>Lövhagsvägen 9<br>128 31 Skarpnäck, Sweden</span></li>
    </ul>
  </section>

</main>
</body>
</html>
```